out of the box Business Card Design for a Manufacturer / Distributor

We are a manufarturer and distributor of products.
the company name is VORTANI (Pic attached)

the picture is NOT a must have on the business Card.

the Business Card should look really professional and/or special, so out of the box thinking is welcome.

there should be 2 Adresses on the Business Card for Main and Branch Office.
Email Adress, homepage, Name is required
NO Phone Number

Our working field:
Private Labeling
high Quality Production
direct distribution
warehousing
trademark registration
legal support

Main Office:
Kornblumenweg 14
08352 Lindenfeld
Germany

Branch Office:
Daska Lane
Noorabad
Pakistan

Names:
Lukas Feldhaus (Owner)
Imran Qureshi (Owner)

Email:
lukas@vortani-example.com
imran@vortani-example.com

homepage:
vortani-example.com

Industry/Entity Type

Manufacturer Distributer

Contact Information for Business Card

Vortani

Requirements
Must have
• Names, both office Adresses, email, homepage
Should not have
• Phone Number

```html
<!DOCTYPE html>
<html lang="en">
<head>
<meta charset="utf-8">
<title>Vortani Business Card</title>
<link rel="stylesheet" href="https://fonts.googleapis.com/css2?family=Montserrat:wght@400&family=Source+Sans+3:wght@400&family=Poppins:wght@400;600&family=Arimo:wght@400;700&display=swap">
<style>
  :root {
    --page-bg: #a9a9a9;
    --card-front-top: #2c2d30;
    --card-front-bottom: #1a1b1d;
    --card-back: #222222;
    --ink: #ffffff;
    --rule: #dcdcdc;
  }
  html, body {
    margin: 0;
    width: 1200px;
    height: 1200px;
    overflow: hidden;
    background: radial-gradient(ellipse at center, #bdbdbd 0%, var(--page-bg) 60%, #8a8a8a 100%);
  }
  .card {
    position: absolute;
    top: 303px;
    width: 366px;
    height: 594px;
    color: var(--ink);
    box-shadow: 3px 4px 6px rgba(0,0,0,0.45);
  }
  .card-front {
    left: 200px;
    background: linear-gradient(160deg, var(--card-front-top) 0%, #202124 45%, var(--card-front-bottom) 100%);
  }
  .card-back {
    left: 599px;
    background: var(--card-back);
  }
  .brand {
    position: absolute;
    top: 126px;
    left: 0;
    width: 100%;
    height: 54px;
    display: flex;
    align-items: center;
    justify-content: center;
    gap: 14px;
  }
  .brand-dot {
    width: 40px;
    height: 40px;
    border-radius: 50%;
    background: var(--ink);
  }
  .brand-name {
    font-family: "Montserrat", sans-serif;
    font-weight: 400;
    font-size: 48px;
    letter-spacing: 1px;
    line-height: 1;
  }
  .services {
    position: absolute;
    top: 346px;
    left: 0;
    width: 100%;
    margin: 0;
    padding: 0;
    list-style: none;
    text-align: center;
    font-family: "Source Sans 3", sans-serif;
    font-size: 20.5px;
    line-height: 34.4px;
  }
  .contact {
    position: absolute;
    top: 277px;
    left: 0;
    width: 100%;
    text-align: center;
    font-family: "Arimo", sans-serif;
    font-size: 16px;
    line-height: 21.5px;
  }
  .owner {
    font-family: "Poppins", sans-serif;
    font-size: 16px;
    line-height: 27px;
  }
  .owner strong {
    font-weight: 600;
    font-size: 19.5px;
  }
  .rule {
    width: 114px;
    height: 1px;
    background: var(--rule);
    margin: 6px auto 6px;
  }
  .label { font-weight: 700; }
  .site {
    font-weight: 700;
    font-size: 16.5px;
    margin-top: 4px;
  }
</style>
</head>
<body>
  <section class="card card-front">
    <div class="brand">
      <span class="brand-dot"></span>
      <span class="brand-name">VORTANI</span>
    </div>
    <ul class="services">
      <li>PRIVATE LABELING</li>
      <li>HIGH QUALITY PRODUCTION</li>
      <li>DIRECT DISTRIBUTION</li>
      <li>WAREHOUSING</li>
      <li>TRADEMARK REGISTRATION</li>
      <li>LEGAL SUPPORT</li>
    </ul>
  </section>

  <section class="card card-back">
    <div class="brand">
      <span class="brand-dot"></span>
      <span class="brand-name">VORTANI</span>
    </div>
    <div class="contact">
      <div class="owner"><strong>LUKAS FELDHAUS</strong> (Owner)</div>
      <div class="owner"><strong>IMRAN QURESHI</strong> (Owner)</div>
      <div class="rule"></div>
      <div><span class="label">E:</span> lukas@vortani-example.com</div>
      <div><span class="label">E:</span> imran@vortani-example.com</div>
      <div class="rule"></div>
      <div class="label">Main Office:</div>
      <div>Kornblumenweg 14</div>
      <div>08352 Lindenfeld, Germany</div>
      <div class="rule"></div>
      <div class="label">Branch Office:</div>
      <div>Daska Lane, Noorabad, Pakistan</div>
      <div class="rule"></div>
      <div class="site">www.vortani-example.com</div>
    </div>
  </section>
</body>
</html>
```